Stylish Business Cards Wanted

- DOUBLE SIDED Design Required -

High end, edgy cards for a corporate and personal stylist. Must include logo,
Name: Belinda Forsey
Title: Director and Stylist
telephone : +61 8 8217 4592
email: belinda@thegarbledger.example
website: thegarbledger.example
Tag: Corporate Workwear & Uniform Specialist | Personal Stylist
Would like nice icons for telephone, email, website

Target Market(s)

Businesses wanting stylish uniforms, people wanting stylish wardrobes

Industry/Entity Type

Corporate Workwear Stylist

Contact Information for Business Card

I would like black, white and gold foiling incorporated in the design - possibly a touch of the other colours on my branding guide attached Name: Belinda Forsey Title: Director and Stylist telephone : +61 8 8217 4592 email: belinda@thegarbledger.example website: thegarbledger.example Tag: Corporate Workwear & Uniform Specialist | Personal Stylist Would like nice icons for telephone, email, website

Font styles to use
Other font styles liked:
• Raleway

Colors

Designer to choose colors to be used in the design.

Requirements
Must have
• Gold foil accents

```html
<!DOCTYPE html>
<html lang="en">
<head>
<meta charset="utf-8">
<title>The Garb Ledger – Business Cards</title>
<link href="https://fonts.googleapis.com/css2?family=Montserrat:wght@400;600&display=swap" rel="stylesheet">
<style>
  :root {
    --backdrop: #141414;
    --card: #242424;
    --white: #f4f4f4;
    --gold: #e2b340;
    --muted: #9a9a9a;
  }
  * { margin: 0; padding: 0; box-sizing: border-box; }
  html, body { width: 1200px; height: 1059px; overflow: hidden; }
  body {
    background: var(--backdrop);
    font-family: "Montserrat", Arial, sans-serif;
    position: relative;
  }
  .card {
    position: absolute;
    background: var(--card);
    border-radius: 16px;
    box-shadow: 0 10px 24px rgba(0,0,0,0.55);
  }
  .card--front { left: 256px; top: 89px; width: 688px; height: 390px; }
  .card--back  { left: 254px; top: 547px; width: 693px; height: 393px; }

  .brand {
    position: absolute;
    display: flex;
    align-items: center;
    gap: 10px;
    font-weight: 600;
    color: var(--white);
    letter-spacing: 0.04em;
    white-space: nowrap;
    transform: translate(-50%, -50%);
  }
  .brand__mark { background: var(--gold); flex: none; }
  .card--front .brand { left: 197px; top: 193px; font-size: 26px; }
  .card--front .brand__mark { width: 14px; height: 14px; }
  .card--back .brand { left: 346px; top: 200px; font-size: 38px; }
  .card--back .brand__mark { width: 20px; height: 20px; }

  .divider {
    position: absolute;
    left: 338px; top: 127px;
    width: 1px; height: 137px;
    background: var(--gold);
  }
  .contact { position: absolute; left: 365px; top: 124px; }
  .contact__name {
    font-size: 25px; font-weight: 600;
    color: var(--gold); letter-spacing: 0.02em;
    line-height: 1.1;
  }
  .contact__title {
    font-size: 17px; color: var(--white);
    margin-top: 2px;
  }
  .contact__list { list-style: none; margin-top: 24px; }
  .contact__item {
    display: flex; align-items: center; gap: 7px;
    font-size: 17px; color: var(--white);
    height: 24.5px;
  }
  .contact__icon { width: 15px; height: 15px; flex: none; }
  .tagline {
    position: absolute;
    left: 0; right: 0; top: 337px;
    text-align: center;
    font-size: 16.5px; color: var(--white);
    letter-spacing: 0.01em;
  }
</style>
</head>
<body>
  <section class="card card--front">
    <div class="brand"><span class="brand__mark"></span>The Garb Ledger</div>
    <div class="divider"></div>
    <div class="contact">
      <h1 class="contact__name">BELINDA FORSEY</h1>
      <p class="contact__title">Director and Stylist</p>
      <ul class="contact__list">
        <li class="contact__item">
          <svg class="contact__icon" viewBox="0 0 16 16" aria-hidden="true"><path fill="#e2b340" d="M3.6 1.2l2.3 2.6-1.4 1.7c.9 2 2.3 3.5 4.1 4.4l1.7-1.4 2.6 2.3-1.5 2.4C6.5 13 2.9 9.3 1.2 2.7z"/><path fill="none" stroke="#e2b340" stroke-width="1.2" d="M9.5 2.5a4 4 0 0 1 4 4M9.5 5a1.6 1.6 0 0 1 1.6 1.6"/></svg>
          +61 8 8217 4592
        </li>
        <li class="contact__item">
          <svg class="contact__icon" viewBox="0 0 16 16" aria-hidden="true"><rect x="0.5" y="3" width="15" height="10.5" fill="#e2b340"/><path d="M0.5 3.5l7.5 5.5 7.5-5.5M0.5 13l5.5-4.5M15.5 13l-5.5-4.5" fill="none" stroke="#242424" stroke-width="1.1"/></svg>
          belinda@thegarbledger.example
        </li>
        <li class="contact__item">
          <svg class="contact__icon" viewBox="0 0 16 16" aria-hidden="true"><circle cx="8" cy="8" r="7.3" fill="#e2b340"/><path fill="#242424" d="M5 3.5c1.5.3 2.3 1.4 1.6 2.5-.8 1-2.4.6-2.2 2.1.2 1.3 1.6 1.4 1.3 3.1L4 12.3C2.3 10.6 2 6 5 3.5zM10 8.5c1.4-.3 2.6.5 2.1 1.9-.4 1.1-1.4 1.8-2.5 2.3-.4-1.5.9-2.4.4-4.2z"/></svg>
          www.thegarbledger.example
        </li>
      </ul>
    </div>
    <p class="tagline">Corporate Workwear &amp; Uniform Specialist | Personal Stylist</p>
  </section>

  <section class="card card--back">
    <div class="brand"><span class="brand__mark"></span>The Garb Ledger</div>
  </section>
</body>
</html>
```